Marine Tourism business need a new product brochure design

We need a design for a DL brochure to promote a new charter marine tour operating out of Hervey Bay, Queensland, Australia. The proposed tour will be conducted within the Tallow Point Marine Park in the waters of world heritage K'Gari (formerly Fraser Island). visit www.bluemerlowcharters.com.au to view current design concepts and colours and fonts etc. The proposed tour details are visible at www.bluemerlowcharters.com.au/tour/reef-outings-2/
The design should promote customers to book and get excited about the tour.

```html
<!DOCTYPE html>
<html lang="en">
<head>
<meta charset="utf-8">
<title>Tallow Point Marine Park – DL Brochure</title>
<link rel="stylesheet" href="https://fonts.googleapis.com/css2?family=Anton&family=Montserrat:ital,wght@0,400;0,600;0,700;1,400;1,600;1,700&display=swap">
<style>
:root{
  --navy:#1c2b8c;
  --navy-deep:#14206b;
  --yellow:#f3d31a;
  --paper:#e8ecf1;
  --paper-warm:#ecebe6;
  --ink:#2b3550;
  --white:#ffffff;
  --stage:#f1f2f4;
}
*{box-sizing:border-box;margin:0;padding:0}
html,body{width:1200px;height:2399px;overflow:hidden;background:var(--stage)}
body{position:relative;font-family:"Montserrat",sans-serif;color:var(--ink)}
.spread{position:absolute;left:50px;width:1100px;height:778px;display:grid;grid-template-columns:repeat(3,1fr);box-shadow:0 18px 40px rgba(20,30,70,.18)}
.spread--outside{top:330px}
.spread--inside{top:1290px}
.panel{position:relative;overflow:hidden;height:778px}
.display{font-family:"Anton",sans-serif;font-weight:400;text-transform:uppercase;letter-spacing:.5px;line-height:1}
.fill{position:absolute}
.fill svg{display:block;width:100%;height:100%}

/* About panel */
.panel--about{background:var(--paper);padding:34px 30px 0}
.about__title{color:var(--navy);font-size:40px;margin-bottom:14px}
.about__copy{font-size:10.5px;font-style:italic;line-height:1.5;margin-bottom:14px}
.about__vessel{color:var(--navy);font-weight:700;font-style:italic;font-size:13px;margin-top:8px}
.about__vessel-copy{font-size:10px;font-style:italic;line-height:1.45}
.about__photos{left:0;bottom:0;width:100%;height:290px}

/* Contact panel */
.panel--contact{background:var(--navy);color:var(--white)}
.contact__curve{inset:0}
.contact__map{position:absolute;left:60px;top:120px;width:250px;height:250px;border-radius:50%;background:radial-gradient(circle at 40% 40%,#ffffff,#d9dde4);border:6px solid var(--white);box-shadow:0 0 0 4px var(--yellow)}
.contact__brand{position:absolute;left:40px;top:430px;display:flex;align-items:center;gap:10px}
.brand__dot{width:26px;height:26px;border-radius:50%;background:var(--white)}
.brand__name{font-family:"Anton",sans-serif;font-size:28px;text-transform:uppercase;color:var(--white);letter-spacing:.5px}
.contact__buzz{position:absolute;left:40px;top:500px;color:var(--yellow);font-size:34px}
.contact__phone{position:absolute;left:40px;top:546px;display:flex;align-items:center;gap:12px;color:var(--yellow);font-family:"Anton",sans-serif;font-size:42px}
.contact__phone svg{width:40px;height:40px}
.contact__details{position:absolute;left:40px;top:626px;list-style:none;font-size:11px;line-height:1.5}
.contact__details li{display:flex;gap:8px;align-items:flex-start;margin-bottom:8px}
.contact__details svg{flex:none;width:14px;height:14px;margin-top:2px}

/* Cover panel */
.panel--cover{background:var(--paper-warm)}
.cover__art{inset:0}
.cover__brand{position:absolute;right:26px;top:46px;display:flex;align-items:center;gap:8px}
.cover__brand .brand__dot{background:var(--navy);width:22px;height:22px}
.cover__brand .brand__name{color:var(--navy);font-size:24px}
.cover__title{position:absolute;left:24px;top:522px;color:var(--navy);font-size:86px}
.cover__band{position:absolute;left:0;right:0;top:622px;background:var(--yellow);padding:8px 24px}
.cover__band span{color:var(--navy);font-size:33px}
.cover__sub{position:absolute;left:24px;right:20px;top:678px;font-size:13px;font-weight:700;color:var(--ink);line-height:1.3}
.cover__url{position:absolute;left:24px;top:730px;font-size:11px;font-weight:700;color:var(--navy)}

/* Charter panel */
.panel--charter{background:var(--navy);color:var(--white);padding:36px 30px 0}
.charter__title{color:var(--yellow);font-size:26px;line-height:1.1;margin-bottom:16px}
.charter__copy{font-size:10.5px;line-height:1.55;margin-bottom:12px}
.charter__note{font-size:10px;font-weight:700;margin-bottom:22px}
.charter__itinerary{color:var(--yellow);font-size:30px;margin-bottom:8px}
.charter__photo{left:0;bottom:0;width:100%;height:260px}

/* Days panel */
.panel--days{background:var(--paper);padding:40px 28px 0}
.tag{display:inline-block;background:var(--yellow);color:var(--navy);font-family:"Anton",sans-serif;text-transform:uppercase;font-size:20px;padding:3px 12px 2px;margin-bottom:10px}
.checklist{list-style:none;font-size:10.5px;line-height:1.45;margin-bottom:18px}
.checklist li{display:flex;gap:7px;margin-bottom:3px}
.checklist li::before{content:"";flex:none;width:9px;height:9px;border:1.5px solid var(--navy);margin-top:3px}
.days__note{font-size:10px;font-weight:700;font-style:italic;line-height:1.4;width:78%}
.days__photos{left:0;bottom:0;width:100%;height:230px}

/* Rates panel */
.panel--rates{background:var(--paper);padding:34px 26px 0}
.panel--rates .tag{font-size:18px;margin-bottom:8px}
.panel--rates .checklist{font-size:9.8px;line-height:1.35;margin-bottom:12px}
.panel--rates .checklist li{margin-bottom:2px}
.panel--rates .checklist li::before{margin-top:2px}
.rates__band{background:var(--navy);color:var(--white);border-radius:0 18px 18px 0;margin:0 -26px 14px 0;padding:8px 14px 10px}
.rates__band .tag{margin:-20px 0 6px}
.rates__price{font-weight:700;font-size:13px}
.rates__small{font-size:9.5px;font-style:italic}
.rates__note{font-size:10px;font-weight:700;font-style:italic;margin:-4px 0 12px}
</style>
</head>
<body>

<section class="spread spread--outside">

  <article class="panel panel--about">
    <h2 class="display about__title">About</h2>
    <p class="about__copy">Our Charter Centre has been named a "Coastal Visitors' Favourite Experience" and more recently received a Harbourside Guest Service Award. We are a family run business that thrives on living life to the fullest and this is demonstrated in the way we deliver our services, be it a dive, snorkel, whale swim or just a water taxi service to K'Gari. We are passionate about scuba training, customer service and ensuring every experience is memorable.</p>
    <h3 class="about__vessel">Our Dive Boat: M.V. Seabright</h3>
    <p class="about__vessel-copy">Our dive and snorkelling vessel is a modern 12m vessel that offers a fast, safe and comfortable ride for all. The vessel is surveyed to carry a maximum of 32 persons.</p>
    <h3 class="about__vessel">Our Whale/Swim Boat: M.V. Coralwind</h3>
    <p class="about__vessel-copy">Our whale watch/swim vessel is a modern 15m catamaran that offers a fast, safe and comfortable ride for all. The vessel is surveyed to carry a maximum of 33 persons.</p>
    <h3 class="about__vessel">Our Live aboard vessel: S.V. Driftline II</h3>
    <p class="about__vessel-copy">Our live aboard vessel is a 18m motor sailing vessel in 2B survey. The vessel is surveyed to carry a maximum of 9 customers and 3 crew.</p>
    <div class="fill about__photos">
      <svg viewBox="0 0 367 290" preserveAspectRatio="none">
        <defs>
          <linearGradient id="deepWater" x1="0" y1="0" x2="0" y2="1">
            <stop offset="0" stop-color="#5b86d0"/><stop offset="1" stop-color="#1c2b8c"/>
          </linearGradient>
        </defs>
        <path d="M0 40 C120 60 250 150 300 290 L0 290 Z" fill="url(#deepWater)" role="img" aria-label="Photo: scuba divers swimming underwater"/>
        <path d="M300 290 C250 150 120 60 0 40" fill="none" stroke="#1c2b8c" stroke-width="10"/>
        <circle cx="70" cy="60" r="46" fill="#9fb9dc" stroke="#ffffff" stroke-width="4" role="img" aria-label="Photo: whale watch vessel at sea"/>
        <circle cx="160" cy="70" r="46" fill="#4f8fc9" stroke="#ffffff" stroke-width="4" role="img" aria-label="Photo: snorkellers in open water"/>
      </svg>
    </div>
  </article>

  <article class="panel panel--contact">
    <div class="fill contact__curve">
      <svg viewBox="0 0 367 778" preserveAspectRatio="none">
        <path d="M367 40 C250 90 215 230 260 360 C230 230 270 100 367 60 Z" fill="#f3d31a"/>
      </svg>
    </div>
    <div class="contact__map" role="img" aria-label="Street map showing the charter office beside the marina"></div>
    <div class="contact__brand">
      <span class="brand__dot"></span>
      <span class="brand__name">Blue Merlow Charters</span>
    </div>
    <p class="display contact__buzz">Give us a buzz</p>
    <p class="contact__phone">
      <svg viewBox="0 0 24 24"><path fill="#f3d31a" d="M6.6 10.8a15.1 15.1 0 0 0 6.6 6.6l2.2-2.2a1 1 0 0 1 1-.25 11.4 11.4 0 0 0 3.6.57 1 1 0 0 1 1 1V20a1 1 0 0 1-1 1A17 17 0 0 1 3 4a1 1 0 0 1 1-1h3.5a1 1 0 0 1 1 1c0 1.250.2 2.45.57 3.57a1 1 0 0 1-.25 1z"/></svg>
      0400 555 218
    </p>
    <ul class="contact__details">
      <li><svg viewBox="0 0 24 24"><path fill="#f3d31a" d="M12 2a7 7 0 0 0-7 7c0 5.25 7 13 7 13s7-7.750 7-13a7 7 0 0 0-7-7zm0 9.5A2.5 2.5 0 1 1 12 6.5a2.5 2.5 0 0 1 0 5z"/></svg><span>The Charter Office<br>Shorehaven Marina, Shorehaven Harbour,<br>Port Callen, Coral Coast 4801</span></li>
      <li><svg viewBox="0 0 24 24"><circle cx="12" cy="12" r="9" fill="none" stroke="#f3d31a" stroke-width="2"/><path d="M3 12h18M12 3c3 3.5 3 14.5 0 18M12 3c-3 3.5-3 14.5 0 18" fill="none" stroke="#f3d31a" stroke-width="1.6"/></svg><span>www.bluemerlowcharters.com.au</span></li>
    </ul>
  </article>

  <article class="panel panel--cover">
    <div class="fill cover__art">
      <svg viewBox="0 0 367 778" preserveAspectRatio="none">
        <defs>
          <linearGradient id="sailSky" x1="0" y1="0" x2="0" y2="1">
            <stop offset="0" stop-color="#dbe4ef"/><stop offset=".7" stop-color="#b9c8dc"/><stop offset="1" stop-color="#5f78a8"/>
          </linearGradient>
        </defs>
        <path d="M0 0 H367 V470 C260 500 120 480 20 390 L0 370 Z" fill="url(#sailSky)" role="img" aria-label="Photo: sailing vessel under full sail with guests on deck"/>
        <path d="M0 370 C60 450 180 510 367 480" fill="none" stroke="#1c2b8c" stroke-width="14"/>
        <path d="M0 390 C80 470 200 520 367 498" fill="none" stroke="#f3d31a" stroke-width="5"/>
        <path d="M0 0 C40 90 10 220 0 280 Z" fill="#f3d31a"/>
        <ellipse cx="260" cy="60" rx="150" ry="78" fill="#ffffff"/>
        <path d="M110 60 A150 78 0 0 0 260 138" fill="none" stroke="#f3d31a" stroke-width="8"/>
      </svg>
    </div>
    <div class="cover__brand">
      <span class="brand__dot"></span>
      <span class="brand__name">Blue Merlow Charters</span>
    </div>
    <h1 class="display cover__title">Tallow</h1>
    <div class="cover__band"><span class="display">Point Marine Park</span></div>
    <p class="cover__sub">The waters of world heritage K'Gari (formerly Fraser Island)</p>
    <p class="cover__url">www.bluemerlowcharters.com.au</p>
  </article>
</section>

<section class="spread spread--inside">

  <article class="panel panel--charter">
    <h2 class="display charter__title">Driftline II K'Gari Skippered<br>Private Charter</h2>
    <p class="charter__copy">Along with your experienced skipper and 2 crew members you will be pampered and entertained as you explore the amazing Tallow Point Marine Park and the western shores of K'Gari (formerly Fraser Island) on our very cool 18m expedition vessel Driftline II. She is an old vessel with a touch of nostalgia and charm with an awesome survey and high level of safety. The vessel accommodates a maximum of 8 customers in 2 cabins, she is comfortable, safe and stable.</p>
    <p class="charter__copy">Along with exploring the Tallow Point Marine Park and the western shores of K'Gari you can expect to experience awesome marine activities like underwater scooters, tubing, kayaking, stand up paddle boards and snorkelling. If you are up to it we can also provide a discover scuba dive experience with one of our instructor crew members.</p>
    <p class="charter__note">NOTE: Each charter can be designed and organised to suit our guests needs.</p>
    <h3 class="display charter__itinerary">Itinerary</h3>
    <p class="charter__copy">Designed with the guests to fulfil that charter dream. <strong>Note: Weather on the day and tides may alter the program slightly.</strong></p>
    <div class="fill charter__photo">
      <svg viewBox="0 0 367 260" preserveAspectRatio="none">
        <defs>
          <linearGradient id="tubeWater" x1="0" y1="0" x2="1" y2="1">
            <stop offset="0" stop-color="#8aa6c9"/><stop offset="1" stop-color="#3d5a9a"/>
          </linearGradient>
        </defs>
        <path d="M0 70 C120 40 260 60 367 20 V260 H0 Z" fill="url(#tubeWater)" role="img" aria-label="Photo: guest riding an inflatable tube across the water"/>
        <path d="M0 90 C40 30 110 10 170 20 C100 30 40 60 0 120 Z" fill="#f3d31a"/>
        <path d="M0 70 C120 40 260 60 367 20" fill="none" stroke="#ffffff" stroke-width="4"/>
      </svg>
    </div>
  </article>

  <article class="panel panel--days">
    <span class="tag">Day 1</span>
    <ul class="checklist">
      <li>Check in 1 hour prior to departure time</li>
      <li>Depart Shorehaven Harbour enjoying morning tea</li>
      <li>2 hour cruise to our first destination for water based activities</li>
      <li>Weigh anchor and enjoy a cruising seafood lunch at around noon</li>
      <li>2 hour cruise to our evening anchorage</li>
      <li>Water based activities</li>
      <li>Sunset drinks and canapes</li>
      <li>Dinner</li>
    </ul>
    <span class="tag">Day 2</span>
    <ul class="checklist">
      <li>Early wake up and weigh anchor then travel to an awesome activity location</li>
      <li>Breakfast</li>
      <li>Water based activities</li>
      <li>Lunch along K'Gari shores</li>
      <li>Arrive Shorehaven Harbour late afternoon</li>
      <li>Disembark</li>
    </ul>
    <p class="days__note">NOTE: Tour options can be modified to suit the guests desires so don't be shy in asking for something special. If we can do it we will!</p>
    <div class="fill days__photos">
      <svg viewBox="0 0 367 230" preserveAspectRatio="none">
        <circle cx="160" cy="120" r="62" fill="#3f86c4" stroke="#ffffff" stroke-width="5" role="img" aria-label="Photo: diver riding an underwater scooter"/>
        <circle cx="285" cy="150" r="66" fill="#e8a15a" stroke="#ffffff" stroke-width="5" role="img" aria-label="Photo: guest on a kayak in clear water"/>
      </svg>
    </div>
  </article>

  <article class="panel panel--rates">
    <div class="rates__band">
      <span class="tag">Rates</span>
      <p class="rates__price">Day Rate: $3000 + GST (max 8 guests)</p>
      <p class="rates__small">Note: Children are welcome aboard for this awesome adventure experience!</p>
    </div>
    <span class="tag">Inclusions</span>
    <ul class="checklist">
      <li>Sailing (weather permitting)</li>
      <li>Underwater Scooter Tours</li>
      <li>Snorkelling</li>
      <li>Kayaking &amp; Stand-up Paddle boards</li>
      <li>Tubing experience</li>
      <li>Fishing experience</li>
      <li>Discover Scuba Experience (By arrangement)</li>
      <li>All Catering and Beverages</li>
      <li>Bedding and towels</li>
      <li>Sunscreen</li>
      <li>Fish and coral reference books</li>
      <li>12V charging facility for battery packs/cameras and the like</li>
    </ul>
    <p class="rates__note">NOTE: Dive/Snorkel Equipment are provided</p>
    <span class="tag">What to bring</span>
    <ul class="checklist">
      <li>Clothing: The temperatures in Nov–March are warm. Shorts and t-shirt day and evening. Pack a long sleeve top for cooler nights. April–Oct are cool in the evenings and mornings so pack layers and a couple of warm sweatshirts. Don't forget the beanie!</li>
      <li>Swimwear</li>
      <li>Sun protection – Hat, sunglasses and a light sun shirt</li>
      <li>Dive/snorkel equipment (the ship will carry an array of spares)</li>
      <li>Toiletries and medication (soap, hand wash and sunscreen are provided)</li>
      <li>Camera of course</li>
      <li>Luggage allowances on-board include 1 x soft personal bag up to 15kg. We prefer soft bags for ease of stowage</li>
      <li>BYO – We allow BYO alcohol. (NOTE: consumption of alcohol is at the discretion of the ships master or his/her nominee)</li>
    </ul>
  </article>
</section>

</body>
</html>
```